Business Cards for Law Office of Denise R. Harlow

I need a business card for my new estate planning law firm. I have attached my logo. I would like a design that is professional but not too formal or stuffy.

Target Market(s)

Professionals (lawyers, doctors, businesswomen) between the age of 30 and 50 who are tech-savvy and educated.

Industry/Entity Type

Lawyer

Contact Information for Business Card

Denise R. Harlow

528 E. 19th Street
7th Floor
New York, NY 10583

Phone: (855) 602-7318
Direct: (917) 463-5071
Email: Denise@DeniseRHarlowLegal.test
www.DeniseRHarlowLegal.test

Font styles to use
Other font styles liked:
• Corbel

Requirements
Must have
• On the front:
• Denise R. Harlow, Esq.
• Owner & Founder
• 528 E. 19th Street
• 7th Floor
• New York, NY 10583
• Phone: (855) 602-7318
• Direct: (917) 463-5071
• Email: denise@deniserharlowlegal.test
• www.deniserharlowlegal.test
• On the back:
• LOGO
Nice to have
• I want it to be professional but not too formal or stuffy. Please choose colors that go with my logo.
Should not have
• I don't want TOO MUCH color. Some color is good, but not too much.

```html
<!DOCTYPE html>
<html lang="en">
<head>
<meta charset="utf-8">
<title>Business Cards – Law Office of Denise R. Harlow</title>
<link rel="stylesheet" href="https://fonts.googleapis.com/css2?family=Open+Sans:wght@400;600&display=swap">
<style>
  :root {
    --stage: #2e2e30;
    --card: #ffffff;
    --purple: #7a2a86;
    --orange: #f08a2c;
    --ink: #1d1d1d;
  }
  * { margin: 0; padding: 0; box-sizing: border-box; }
  html, body { width: 1200px; height: 880px; overflow: hidden; }
  body {
    background: var(--stage);
    font-family: "Open Sans", "Segoe UI", sans-serif;
    position: relative;
  }
  .card {
    position: absolute;
    width: 640px;
    height: 366px;
    background: var(--card);
    border-radius: 22px;
    overflow: hidden;
    box-shadow: 0 18px 40px rgba(0,0,0,.45);
  }
  .card--back { left: 70px; top: 50px; }
  .card--front { left: 490px; top: 470px; }

  .card__band {
    position: absolute; left: 0; right: 0; bottom: 0;
    height: 14px; display: flex;
  }
  .card__band-purple { background: var(--purple); }
  .card__band-orange { background: var(--orange); flex: 1; }
  .card--back .card__band-purple { width: 45%; }
  .card--front .card__band-purple { width: 52%; }

  .firm-name {
    position: absolute; left: 0; right: 0;
    text-align: center;
    color: var(--purple);
    font-weight: 600;
    text-transform: uppercase;
    letter-spacing: 2px;
    line-height: 1.15;
  }
  .firm-name__small { display: block; font-size: 17px; letter-spacing: 4px; }
  .firm-name__large { display: block; font-size: 40px; }
  .card--back .firm-name { top: 120px; }
  .card--front .firm-name { top: 58px; }

  .details {
    position: absolute; left: 40px; right: 40px; top: 205px;
    display: flex; align-items: center; justify-content: center;
  }
  .person {
    text-align: right;
    padding-right: 22px;
    color: var(--ink);
    font-size: 15px;
    line-height: 1.4;
  }
  .person__name {
    color: var(--purple);
    font-weight: 600;
    font-size: 19px;
    letter-spacing: 1px;
    text-transform: uppercase;
  }
  .divider { width: 2px; height: 104px; background: var(--purple); }
  .contact { list-style: none; padding-left: 18px; font-size: 14px; color: var(--ink); }
  .contact__item { display: flex; align-items: center; gap: 8px; line-height: 1.75; }
  .contact__icon { width: 17px; height: 17px; flex: none; }
</style>
</head>
<body>

  <section class="card card--back" aria-label="Card back">
    <h1 class="firm-name">
      <span class="firm-name__small">Law Office of</span>
      <span class="firm-name__large">Denise R. Harlow</span>
    </h1>
    <div class="card__band"><div class="card__band-purple"></div><div class="card__band-orange"></div></div>
  </section>

  <section class="card card--front" aria-label="Card front">
    <h2 class="firm-name">
      <span class="firm-name__small">Law Office of</span>
      <span class="firm-name__large">Denise R. Harlow</span>
    </h2>

    <div class="details">
      <address class="person" style="font-style:normal">
        <div class="person__name">Denise R. Harlow</div>
        528 E. 19th Street<br>
        7th Floor<br>
        New York, NY 10583
      </address>
      <div class="divider"></div>
      <ul class="contact">
        <li class="contact__item">
          <svg class="contact__icon" viewBox="0 0 16 16" aria-hidden="true"><rect width="16" height="16" rx="2" fill="var(--orange)"/><path d="M4 4.5c0 4 3.5 7.5 7.5 7.5l1-2-2-1-1 1c-1.2-.6-2.4-1.8-3-3l1-1-1-2z" fill="#fff"/></svg>
          (855) 602-7318
        </li>
        <li class="contact__item">
          <svg class="contact__icon" viewBox="0 0 16 16" aria-hidden="true"><rect width="16" height="16" rx="2" fill="var(--orange)"/><rect x="5" y="3" width="6" height="10" rx="1" fill="none" stroke="#fff" stroke-width="1.3"/><circle cx="8" cy="11" r=".8" fill="#fff"/></svg>
          (917) 463-5071
        </li>
        <li class="contact__item">
          <svg class="contact__icon" viewBox="0 0 16 16" aria-hidden="true"><rect width="16" height="16" rx="2" fill="var(--orange)"/><rect x="3" y="4.5" width="10" height="7" fill="none" stroke="#fff" stroke-width="1.2"/><path d="M3 4.5l5 4 5-4" fill="none" stroke="#fff" stroke-width="1.2"/></svg>
          Denise@DeniseRHarlowLegal.test
        </li>
        <li class="contact__item">
          <svg class="contact__icon" viewBox="0 0 16 16" aria-hidden="true"><rect width="16" height="16" rx="2" fill="var(--orange)"/><circle cx="8" cy="8" r="4.8" fill="none" stroke="#fff" stroke-width="1.1"/><ellipse cx="8" cy="8" rx="2" ry="4.8" fill="none" stroke="#fff" stroke-width="1"/><path d="M3.2 8h9.6" stroke="#fff" stroke-width="1"/></svg>
          www.DeniseRHarlowLegal.test
        </li>
      </ul>
    </div>

    <div class="card__band"><div class="card__band-purple"></div><div class="card__band-orange"></div></div>
  </section>

</body>
</html>
```